!!! THIS PROJECT IS FOR ODETTE ONLY !!!
Hi Odette,
Hope you are well.
Please help me to create a new poster for my new dishes.
Poster size is A2 (420mmx595mm)
I want 1 poster design to showcase all 3 new dishes.
1. Bánh Mì $9.50 (I've sent all photos of this but you don't need to use all photos - its all up to you to make the design fit)
- Lemongrass Chicken
- Lemongrass Beef
- BBQ Pork
- Tofu
2. Egg Noodle with Crispy Skin Chicken (With Soup / Dry) $16.50
3. Rice with Crispy Skin Chicken. $16.50

```html
<!DOCTYPE html>
<html lang="en">
<head>
<meta charset="utf-8">
<title>Lantern Bowl – New Dishes Poster</title>
<link href="https://fonts.googleapis.com/css2?family=Archivo+Black&family=Oswald:wght@700&family=Montserrat:wght@700&display=swap" rel="stylesheet">
<style>
  :root {
    --bg-top: #e3e3e3;
    --bg-top-light: #f1f1f1;
    --bg-mid: #eeeeee;
    --bg-bottom: #ebebeb;
    --plane-light: #f8f8f8;
    --plane-shade: #dedede;
    --podium: #d9d9d9;
    --ink: #111111;
    --price: #555555;
    --label: #4a4a4a;
    --brand: #f39221;
    --bread: #d9a05a;
    --bread-light: #eecb95;
    --herb: #6f9a3a;
    --beef: #6b4230;
    --broth: #cfae55;
    --roast: #c9672b;
    --carrot: #ec7a38;
    --rice: #f6f3ea;
    --lettuce: #b9d38f;
  }
  * { margin: 0; padding: 0; box-sizing: border-box; }
  html, body { width: 846px; height: 1200px; overflow: hidden; background: var(--bg-mid); }
  .poster { position: relative; width: 846px; height: 1200px; overflow: hidden; font-family: "Archivo Black", sans-serif; color: var(--ink); }

  .section { position: absolute; left: 0; width: 846px; overflow: hidden; }
  .section--banh-mi { top: 0; height: 400px; background: linear-gradient(160deg, var(--bg-top-light), var(--bg-top)); }
  .section--noodle { top: 400px; height: 400px; background: var(--bg-mid); }
  .section--rice { top: 800px; height: 400px; background: linear-gradient(180deg, #e4e4e4, #f2f2f2 45%, var(--bg-bottom)); }
  .planes { position: absolute; inset: 0; width: 846px; height: 400px; }

  .podium { position: absolute; left: 261px; top: 296px; width: 480px; height: 104px; background: linear-gradient(180deg, #e8e8e8, var(--podium)); }
  .podium-side { position: absolute; left: 740px; top: 346px; width: 106px; height: 54px; background: #e0e0e0; }

  .photo { position: absolute; box-shadow: 0 8px 14px rgba(0,0,0,0.16); }
  .photo--roll { border-radius: 46% 46% 10px 10px / 70% 70% 10px 10px;
    background: linear-gradient(180deg, var(--bread) 0%, var(--bread-light) 28%, var(--herb) 46%, #b86a3c 62%, var(--bread-light) 78%, #f2f2f2 86%, #e6e6e6 100%); }
  .photo--chicken-roll { left: 84px; top: 63px; width: 171px; height: 68px; }
  .photo--pork-roll { left: 86px; top: 186px; width: 165px; height: 70px; }
  .photo--tofu-roll { left: 84px; top: 306px; width: 171px; height: 73px; }
  .photo--beef-roll { left: 438px; top: 112px; width: 420px; height: 191px; border-radius: 120px 0 18px 40px / 90px 0 18px 40px;
    background: linear-gradient(180deg, var(--bread) 0%, var(--bread-light) 20%, var(--herb) 36%, var(--beef) 52%, #7d5136 66%, #f5f5f5 76%, #e4e4e4 100%); }

  .roll-label { position: absolute; font-family: "Montserrat", sans-serif; font-weight: 700; color: var(--label); font-size: 17px; line-height: 18px; text-align: center; letter-spacing: 0.2px; }
  .roll-label--chicken { left: 71px; top: 137px; width: 200px; }
  .roll-label--pork { left: 71px; top: 262px; width: 200px; }
  .roll-label--tofu { left: 71px; top: 384px; width: 200px; }
  .roll-label--beef { left: 590px; top: 317px; width: 210px; }

  .brand { position: absolute; left: 360px; top: 56px; width: 128px; height: 128px; display: flex; flex-direction: column; align-items: center; justify-content: center; gap: 8px; }
  .brand-dot { width: 22px; height: 22px; border-radius: 50%; background: var(--brand); }
  .brand-name { font-family: "Archivo Black", sans-serif; color: var(--brand); font-size: 16px; line-height: 18px; text-align: center; }

  .dish-title { position: absolute; font-size: 34px; line-height: 36px; text-align: center; }
  .dish-note { display: block; font-size: 20px; line-height: 30px; }
  .price { position: absolute; font-family: "Oswald", sans-serif; font-weight: 700; color: var(--price); font-size: 64px; line-height: 64px; letter-spacing: -1px; }
  .price .currency { font-size: 34px; vertical-align: 24px; margin-right: 1px; }

  .dish-title--banh-mi { left: 271px; top: 228px; font-size: 35px; text-align: left; }
  .price--banh-mi { left: 276px; top: 274px; }

  .photo--noodle-bowl { left: -14px; top: 130px; width: 280px; height: 280px; border-radius: 50%;
    background: radial-gradient(circle at 45% 45%, #d9b85e 0%, var(--broth) 45%, #b7a24c 62%, #f3f3f3 70%, #e8e8e8 100%); }
  .photo--chicken-plate { left: 276px; top: 18px; width: 230px; height: 330px; border-radius: 26px; transform: rotate(-28deg);
    background: linear-gradient(200deg, #f6f6f6 0%, #f6f6f6 12%, #d27a3a 24%, var(--roast) 50%, var(--carrot) 70%, #f4f4f4 84%, #efefef 100%); }

  .dish-title--noodle { left: 543px; top: 94px; width: 262px; }
  .price--noodle { left: 597px; top: 236px; }

  .dish-title--rice { left: 62px; top: 102px; width: 252px; }
  .price--rice { left: 112px; top: 218px; }

  .photo--rice-plate { left: 318px; top: 120px; width: 470px; height: 300px; border-radius: 26px; transform: rotate(11deg);
    background: linear-gradient(90deg, #f5f5f5 0%, var(--rice) 14%, #fbfaf6 34%, var(--roast) 48%, #d48a4a 62%, var(--carrot) 76%, var(--lettuce) 90%, #f2f2f2 100%); }
</style>
</head>
<body>
<main class="poster">

  <section class="section section--banh-mi">
    <svg class="planes" viewBox="0 0 846 400" aria-hidden="true">
      <polygon points="0,92 322,114 0,136" fill="#f7f7f7"/>
    </svg>
    <div class="podium"></div>
    <div class="podium-side"></div>

    <div class="photo photo--roll photo--chicken-roll" role="img" aria-label="Lemongrass chicken bánh mì on a white plate"></div>
    <p class="roll-label roll-label--chicken">LEMONGRASS<br>CHICKEN</p>

    <div class="photo photo--roll photo--pork-roll" role="img" aria-label="BBQ pork bánh mì on a white plate"></div>
    <p class="roll-label roll-label--pork">BBQ PORK</p>

    <div class="photo photo--roll photo--tofu-roll" role="img" aria-label="Tofu bánh mì on a white plate"></div>
    <p class="roll-label roll-label--tofu">TOFU</p>

    <div class="brand">
      <span class="brand-dot"></span>
      <span class="brand-name">LANTERN<br>BOWL</span>
    </div>

    <h2 class="dish-title dish-title--banh-mi">Bánh Mì</h2>
    <p class="price price--banh-mi"><span class="currency">$</span>9.50</p>

    <div class="photo photo--beef-roll" role="img" aria-label="Lemongrass beef bánh mì with coriander and spring onion on a long white plate"></div>
    <p class="roll-label roll-label--beef">LEMONGRASS BEEF</p>
  </section>

  <section class="section section--noodle">
    <svg class="planes" viewBox="0 0 846 400" aria-hidden="true">
      <polygon points="486,0 846,0 846,240 590,400 390,400 846,175 846,120" fill="var(--plane-light)"/>
      <polygon points="486,0 540,0 846,210 846,240" fill="var(--plane-shade)" opacity="0.5"/>
    </svg>
    <div class="photo photo--noodle-bowl" role="img" aria-label="Bowl of egg noodle soup with chives, coriander and fried shallots"></div>
    <div class="photo photo--chicken-plate" role="img" aria-label="Crispy skin chicken with pickled carrot and lettuce on a white plate"></div>
    <h2 class="dish-title dish-title--noodle">Egg Noodle with Crispy Skin Chicken<span class="dish-note">(With Soup / Dry)</span></h2>
    <p class="price price--noodle"><span class="currency">$</span>16.50</p>
  </section>

  <section class="section section--rice">
    <svg class="planes" viewBox="0 0 846 400" aria-hidden="true">
      <polygon points="0,0 846,0 846,160 0,170" fill="#e9e9e9"/>
      <polygon points="0,70 220,0 0,0" fill="#dcdcdc"/>
    </svg>
    <h2 class="dish-title dish-title--rice">Rice with Crispy Skin Chicken</h2>
    <p class="price price--rice"><span class="currency">$</span>16.50</p>
    <div class="photo photo--rice-plate" role="img" aria-label="Steamed rice with crispy skin chicken, lettuce, carrot and cucumber on a white plate"></div>
  </section>

</main>
</body>
</html>
```